Massage Certificate Design that is Elegant, Modern, Hip with a "Pop"

We need a massage certificate for our Chiropractic office. Our brand feel is modern, clean, hip, and bold. Something that has some "pop" to it and that is different. We play dance music on Fridays, we care for kids and families, and provide vitality care, not just about neck and back pain. We would like to see a design that incorporates our logo along with a burnt orange accent color, tan, white, and black. We attached a sample certificate. On one side we would like to have it designate the massage price of $50, a space to write in who the certificate is for, who it is from, a space to write in an expiration date. On the back of the certificate we would like to have the office contact info. 4173 W. Marlow Lane, C204, Fairhaven, AZ 85099. A map of the location.
Phone: (480) 731-2946
Facebook
Twitter

Target Market(s)

Moms, Wellness Minded, Vitality Focused, Looking for reducing stress and muscle stiffness

Industry/Entity Type

Health And Wellness

Colors
f37122
000000
fefefe

Requirements
Must have
• Burnt orange accent color, tan, black, and white colors used.

```html
<!DOCTYPE html>
<html lang="en">
<head>
<meta charset="utf-8">
<title>Gift Certificate – Brightvale Family Chiropractic</title>
<link href="https://fonts.googleapis.com/css2?family=Oswald:wght@500;600&family=Lato:wght@400;700;900&display=swap" rel="stylesheet">
<style>
  :root{
    --orange:#f37122;
    --orange-deep:#d9560b;
    --black:#111111;
    --charcoal:#2a2a2a;
    --white:#fefefe;
    --tan:#d8c3a5;
    --page:#e4e4e4;
    --sky:#5b93d6;
    --sky-light:#c9def3;
    --map:#e8e3d8;
  }
  *{box-sizing:border-box;margin:0;padding:0}
  html,body{width:1200px;height:1170px;overflow:hidden;background:var(--page)}
  .sheet{position:relative;width:1200px;height:1170px}
  .card{position:absolute;left:53px;width:1097px;height:490px;overflow:hidden;
        box-shadow:0 6px 14px rgba(0,0,0,.35);background:var(--black)}
  .card--front{top:64px}
  .card--back{top:614px}
  .card__art{position:absolute;inset:0;width:1097px;height:490px}
  .tagline{position:absolute;left:23px;top:86px;line-height:1}
  .tagline__accent{display:block;font-family:'Oswald',sans-serif;font-weight:600;font-size:27px;color:var(--orange);letter-spacing:.2px}
  .tagline__main{display:block;margin-top:8px;font-family:'Lato',sans-serif;font-weight:400;font-size:34px;color:var(--black);letter-spacing:.3px}
  .brand{position:absolute;left:372px;top:104px;width:140px;display:flex;align-items:center;gap:8px;
         font-family:'Lato',sans-serif;font-weight:700;font-size:11px;line-height:1.25;color:var(--charcoal);text-transform:uppercase}
  .brand__dot{flex:none;width:12px;height:12px;border-radius:50%;background:var(--orange)}
  .brand-divider{position:absolute;left:361px;top:72px;width:1px;height:100px;background:#bdbdbd}
  .cert-title{position:absolute;left:23px;top:182px;font-family:'Oswald',sans-serif;font-weight:600;font-size:43px;color:var(--orange);letter-spacing:.5px;line-height:1}
  .write-line{position:absolute;left:23px;width:400px;border-top:1.5px dashed #555}
  .price{position:absolute;left:466px;top:188px;width:148px;height:148px;display:flex;align-items:center;justify-content:center;
         font-family:'Lato',sans-serif;font-weight:900;font-size:58px;color:var(--black)}
  .contact{position:absolute;left:22px;bottom:16px;display:flex;align-items:center;gap:10px;
           font-family:'Lato',sans-serif;font-size:16px;color:var(--white)}
  .contact__item{display:flex;align-items:center;gap:7px;margin-right:8px}
  .contact svg{width:17px;height:17px}
  .ghost-brand{position:absolute;left:330px;top:318px;font-family:'Lato',sans-serif;font-weight:700;font-size:28px;
               color:var(--orange-deep);opacity:.55;text-transform:uppercase;line-height:1.1;letter-spacing:1px}
</style>
</head>
<body>
<main class="sheet">

  <section class="card card--front">
    <svg class="card__art" viewBox="0 0 1097 490">
      <defs>
        <linearGradient id="sky" x1="0" y1="0" x2="0" y2="1">
          <stop offset="0" stop-color="var(--sky)"/>
          <stop offset=".55" stop-color="var(--sky-light)"/>
          <stop offset="1" stop-color="#f4f4f4"/>
        </linearGradient>
      </defs>
      <polygon points="0,60 640,8 700,440 0,410" fill="var(--white)"/>
      <line x1="0" y1="58" x2="640" y2="7" stroke="var(--orange)" stroke-width="4"/>
      <line x1="0" y1="412" x2="700" y2="443" stroke="var(--orange)" stroke-width="5"/>
      <path d="M582,0 Q452,250 682,490" fill="none" stroke="var(--orange)" stroke-width="22"/>
      <path d="M604,0 Q474,250 704,490" fill="none" stroke="var(--black)" stroke-width="14"/>
      <path d="M612,0 Q482,250 712,490 L1097,490 L1097,0 Z" fill="url(#sky)" role="img" aria-label="Photo of a smiling family of four, parents holding two young children, against a blue sky"/>
      <circle cx="540" cy="262" r="78" fill="var(--orange)" stroke="var(--white)" stroke-width="4"/>
      <circle cx="540" cy="262" r="68" fill="none" stroke="var(--white)" stroke-width="1.5" stroke-dasharray="3 4"/>
    </svg>
    <div class="tagline">
      <span class="tagline__accent">HEALTHCARE THE WAY NATURE</span>
      <span class="tagline__main">INTENDED IT TO BE</span>
    </div>
    <div class="brand-divider"></div>
    <div class="brand"><span class="brand__dot"></span><span>Brightvale Family Chiropractic</span></div>
    <h1 class="cert-title">GIFT CERTIFICATE</h1>
    <div class="write-line" style="top:274px"></div>
    <div class="write-line" style="top:318px"></div>
    <div class="write-line" style="top:364px"></div>
    <div class="price">$50</div>
    <div class="contact">
      <span class="contact__item">
        <svg viewBox="0 0 24 24"><path fill="var(--orange)" d="M6.6 10.8a15.1 15.1 0 0 0 6.6 6.6l2.2-2.2a1 1 0 0 1 1-.25 11.4 11.4 0 0 0 3.6.57 1 1 0 0 1 1 1V20a1 1 0 0 1-1 1A17 17 0 0 1 3 4a1 1 0 0 1 1-1h3.5a1 1 0 0 1 1 1c0 1.25.2 2.45.57 3.57a1 1 0 0 1-.25 1z"/></svg>
        (480) 731-2946
      </span>
      <span class="contact__item">
        <svg viewBox="0 0 24 24"><path fill="var(--orange)" d="M12 2a7 7 0 0 0-7 7c0 5.25 7 13 7 13s7-7.75 7-13a7 7 0 0 0-7-7zm0 9.5A2.5 2.5 0 1 1 12 6.5a2.5 2.5 0 0 1 0 5z"/></svg>
        4173 W. Marlow Lane, C204, Fairhaven, AZ 85099
      </span>
    </div>
  </section>

  <section class="card card--back">
    <svg class="card__art" viewBox="0 0 1097 490">
      <defs>
        <linearGradient id="orangeField" x1="0" y1="0" x2="1" y2="0">
          <stop offset="0" stop-color="var(--orange-deep)"/>
          <stop offset=".5" stop-color="var(--orange)"/>
          <stop offset="1" stop-color="var(--orange-deep)"/>
        </linearGradient>
        <linearGradient id="topBand" x1="0" y1="0" x2="0" y2="1">
          <stop offset="0" stop-color="var(--black)"/>
          <stop offset="1" stop-color="#3a3a3a"/>
        </linearGradient>
      </defs>
      <rect width="1097" height="80" fill="url(#topBand)"/>
      <polygon points="0,64 1097,30 1097,440 0,410" fill="var(--white)"/>
      <polygon points="0,70 1097,37 1097,433 0,404" fill="url(#orangeField)"/>
      <circle cx="879" cy="243" r="176" fill="var(--black)"/>
      <circle cx="879" cy="243" r="161" fill="var(--map)" role="img" aria-label="Street map showing the office location near the freeway"/>
    </svg>
    <div class="ghost-brand">Brightvale Family<br>Chiropractic</div>
    <div class="contact">
      <span class="contact__item">
        <svg viewBox="0 0 24 24"><path fill="var(--orange)" d="M6.6 10.8a15.1 15.1 0 0 0 6.6 6.6l2.2-2.2a1 1 0 0 1 1-.25 11.4 11.4 0 0 0 3.6.57 1 1 0 0 1 1 1V20a1 1 0 0 1-1 1A17 17 0 0 1 3 4a1 1 0 0 1 1-1h3.5a1 1 0 0 1 1 1c0 1.25.2 2.45.57 3.57a1 1 0 0 1-.25 1z"/></svg>
        (480) 731-2946
      </span>
      <span class="contact__item">
        <svg viewBox="0 0 24 24"><path fill="var(--orange)" d="M12 2a7 7 0 0 0-7 7c0 5.25 7 13 7 13s7-7.75 7-13a7 7 0 0 0-7-7zm0 9.5A2.5 2.5 0 1 1 12 6.5a2.5 2.5 0 0 1 0 5z"/></svg>
        4173 W. Marlow Lane, C204, Fairhaven, AZ 85099
      </span>
    </div>
  </section>

</main>
</body>
</html>
```